Accounting Business needs double sided DL flyer design

We need a double sided DL flyer designed,
Front side with logo, web address and our short intro.
Backside to have a list of services.
Our colours are blue and a concrete grey colour. Look at our website for a feel for our colour scheme.
www.lanternwellgroup.com.au
I have included the pic from our website to possibly use but we are also open to new creative ideas.
Target Market(s)
Our target market are proactive business owners, particularly in the wine and hospitality industry.
Industry/Entity Type
Business
Look and feel

```html
<!DOCTYPE html>
<html lang="en">
<head>
<meta charset="utf-8">
<title>Lanternwell Group – DL Flyer</title>
<link href="https://fonts.googleapis.com/css2?family=Jost:ital,wght@0,400;0,500;0,600;1,400;1,600&display=swap" rel="stylesheet">
<style>
  :root {
    --blue: #2f72b8;
    --blue-deep: #1f5ea3;
    --navy: #1d3f7a;
    --concrete: #cfd3d6;
    --concrete-dark: #a9adb0;
    --mist: #e3eef4;
    --paper: #f7f9fa;
    --ink: #4a4d52;
    --stage: #c9d6df;
  }
  * { box-sizing: border-box; margin: 0; padding: 0; }
  html, body { width: 1200px; height: 1200px; overflow: hidden; }
  body {
    background: var(--stage);
    font-family: "Jost", "Futura", sans-serif;
    color: var(--ink);
    position: relative;
  }
  .flyer-spread {
    position: absolute;
    left: 70px; top: 230px;
    display: flex; gap: 20px;
  }
  .flyer-page {
    position: relative;
    width: 520px; height: 740px;
    background: var(--paper);
    overflow: hidden;
    box-shadow: 0 12px 30px rgba(40, 60, 80, .18);
  }
  .page-shapes { position: absolute; inset: 0; }

  /* front page */
  .brand-name {
    position: absolute; right: 18px; top: 22px;
    text-align: right; color: var(--navy); white-space: nowrap;
  }
  .brand-name .name {
    font-weight: 600; font-size: 15px; letter-spacing: 1.4px; text-transform: uppercase;
  }
  .brand-name .tagline {
    font-size: 6.5px; letter-spacing: 2px; text-transform: uppercase; margin-top: 2px;
  }
  .contact-address {
    position: absolute; left: 32px; top: 540px; width: 210px;
    color: var(--blue); font-style: italic; font-size: 16px; line-height: 1.35;
  }
  .contact-divider {
    position: absolute; left: 258px; top: 525px; width: 1px; height: 140px;
    background: var(--concrete);
  }
  .contact-digital {
    position: absolute; left: 276px; top: 560px; color: var(--blue);
  }
  .contact-row { display: flex; align-items: center; gap: 8px; white-space: nowrap; }
  .contact-row.web { font-size: 12.5px; }
  .contact-row.phone { font-size: 26px; margin-top: 10px; letter-spacing: 1px; }
  .contact-row svg { flex: none; }

  /* back page */
  .copy-block {
    position: absolute; left: 40px; width: 440px;
    font-size: 15px; line-height: 1.35; font-style: italic;
  }
  .copy-block h2 {
    font-size: 15px; font-weight: 600; font-style: italic; color: #3d4045;
  }
  .copy-intro { top: 110px; }
  .copy-detail { top: 345px; }
  .footer-brand {
    position: absolute; left: 0; right: 0; top: 640px;
    text-align: center; color: #ffffff;
  }
  .footer-brand .name {
    font-weight: 600; font-size: 22px; letter-spacing: 2px; text-transform: uppercase;
  }
  .footer-brand .tagline {
    font-size: 8px; letter-spacing: 3px; text-transform: uppercase; margin-top: 3px;
  }
</style>
</head>
<body>
  <main class="flyer-spread">
    <section class="flyer-page flyer-front">
      <svg class="page-shapes" width="520" height="740" viewBox="0 0 520 740">
        <defs>
          <linearGradient id="concrete-tone" x1="0" y1="0" x2="1" y2="1">
            <stop offset="0" stop-color="#e9ebec"/>
            <stop offset="0.6" stop-color="#cdd1d3"/>
            <stop offset="1" stop-color="#a3a8ab"/>
          </linearGradient>
        </defs>
        <polygon points="0,0 60,0 0,60" fill="var(--blue)"/>
        <polygon role="img" aria-label="Photo of grey concrete steps and wall" points="60,0 180,0 520,390 520,470 0,470 0,60" fill="url(#concrete-tone)"/>
        <polygon points="180,0 260,0 520,300 520,390" fill="var(--blue)"/>
        <polygon points="0,310 0,470 240,470" fill="var(--blue-deep)"/>
        <rect x="0" y="470" width="520" height="36" fill="var(--mist)"/>
        <rect x="0" y="688" width="520" height="52" fill="var(--blue)"/>
      </svg>
      <div class="brand-name">
        <div class="name">Lanternwell Group</div>
        <div class="tagline">Business Advisors &amp; Accountants</div>
      </div>
      <address class="contact-address">
        12 Harlow Street<br>
        Eastbrook Vic 3940<br>
        (By Appointment Only)<br>
        PO Box 5812<br>
        Eastbrook Vic 394
      </address>
      <div class="contact-divider"></div>
      <div class="contact-digital">
        <div class="contact-row web">
          <svg width="18" height="18" viewBox="0 0 20 20" fill="none" stroke="currentColor" stroke-width="1.6">
            <circle cx="10" cy="10" r="8.5"/><ellipse cx="10" cy="10" rx="3.8" ry="8.5"/>
            <line x1="1.5" y1="10" x2="18.5" y2="10"/>
          </svg>
          <span>hello@lanternwellgroup.com.au</span>
        </div>
        <div class="contact-row phone">
          <svg width="22" height="22" viewBox="0 0 24 24" fill="currentColor">
            <path d="M6.6 10.8a15.1 15.1 0 0 0 6.6 6.6l2.2-2.2a1 1 0 0 1 1-.25 11.4 11.4 0 0 0 3.6.57 1 1 0 0 1 1 1V20a1 1 0 0 1-1 1A17 17 0 0 1 3 4a1 1 0 0 1 1-1h3.5a1 1 0 0 1 1 1c0 1.25.2 2.45.57 3.6a1 1 0 0 1-.25 1z"/>
          </svg>
          <span>0491 570 228</span>
        </div>
      </div>
    </section>

    <section class="flyer-page flyer-back">
      <svg class="page-shapes" width="520" height="740" viewBox="0 0 520 740">
        <rect x="0" y="0" width="520" height="70" fill="var(--mist)"/>
        <rect x="0" y="290" width="520" height="34" fill="var(--mist)"/>
        <rect x="0" y="545" width="520" height="40" fill="var(--mist)"/>
        <rect x="0" y="600" width="520" height="140" fill="var(--blue)"/>
      </svg>
      <div class="copy-block copy-intro">
        <h2>Lorem ipsum:</h2>
        <p>dolor sit amet, consectetur adipiscing elit. Morbi imperdiet mauris odio, a porttitor ex pretium a. Duis a nisl tincidunt, hendrerit augue et, auctor quam. Donec non augue tellus. Nullam ac eros vitae massa rhoncus egestas. Praesent suscipit eu-ismod sem, eu ultricies arcu iaculis ut. Nullam tortor ipsum, lacinia vitae maximus congue, maximus in velit. Etiam rutrum nisl nec scelerisque consequat.</p>
      </div>
      <div class="copy-block copy-detail">
        <h2>Nulla lacinia:</h2>
        <p>erat vel semper gravida. Nulla auctor mollis sem, sit amet dignissim nunc varius a. Proin finibus, diam ultrices mollis tristique, lectus leo tristique odio, eu porta diam urna sit amet risus. Integer gravida, nunc eget faucibus cursus, enim libero convallis metus, nec blandit arcu sem vitae orci. Nullam eu libero quis ligula faucibus ultricies id eget velit. In ullamcorper sapien et ultricies malesuada. Etiam magna metus, molestie eget massa quis, porta blandit quam.</p>
      </div>
      <div class="footer-brand">
        <div class="name">Lanternwell Group</div>
        <div class="tagline">Business Advisors &amp; Accountants</div>
      </div>
    </section>
  </main>
</body>
</html>
```